Cat-products company needs smart, yet endearing, business card

We need a business card design for a new, but up-and-running, business based in Honolulu, Hawaii. The business is Purrlane Nest Co. Our first product is the most environmentally-friendly cat grass kit ever seen on the planet. Future products, currently in the R&D phase, will include a variety of exciting cat scratchers. We also do consulting work to help apartment-dwellers make their home more cat-friendly and, in the future, plan on doing full, custom installs of structure to create high walkways for cats.

Target Market(s)

Middle-aged, apartment-dwelling, middle-class workers who own 1 or more cats and who dote on them.

Industry/Entity Type

Pet Care

Contact Information for Business Card

A striking, professional, yet warm and friendly design is what we're after.

Font styles to use
Serif
Sans Serif
Other font styles liked:
• Comfortaa

Colors

Designer to choose colors to be used in the design.

Requirements
Must have
• The company logo: (see attachment)
• The company name: Purrlane Nest Co
• The web address: www.purrlanenestco.example
• Email: support@purrlanenestco.example
• Phone: +1 (808) 555 0172
• Update (Fri Jun 30 3017 7:45pm Hawaii Time) I would like, is possible, uploaded picture of the cat grass kit on the back of the card with some text along the lines of: Purrlane Nest Co - Where The Freshest Kitty Sprouts Begin
Nice to have
• A cat picture, cartoon, real or silhouette that illustrates cats in action and/or relaxing; ie using the apartment space to live, play and relax in and being well-contented.
• Most of the website is done in the font: Comfortaa. It might be nice to continue using this for brand consistency.
Should not have
• Hard-to-read fonts.

```html
<!DOCTYPE html>
<html lang="en">
<head>
<meta charset="utf-8">
<title>Purrlane Nest Co — Business Card</title>
<link rel="stylesheet" href="https://fonts.googleapis.com/css2?family=Comfortaa:wght@400;600;700&display=swap">
<style>
  :root {
    --backdrop: #6f7a80;
    --card: #ffffff;
    --brand-orange: #f5a81c;
    --brand-brown: #4b2b20;
    --ink: #1f1f1f;
    --kraft: #cdbd9c;
    --kraft-light: #ddd0b4;
    --grass: #8bbd4a;
    --card-shadow: 0 18px 30px rgba(0,0,0,.35);
  }
  * { box-sizing: border-box; margin: 0; padding: 0; }
  html, body {
    width: 1200px; height: 900px; overflow: hidden;
    background: var(--backdrop);
    font-family: "Comfortaa", sans-serif;
  }
  .stage { position: relative; width: 1200px; height: 900px; }
  .card {
    position: absolute;
    width: 540px; height: 310px;
    background: var(--card);
    border-radius: 16px;
    box-shadow: var(--card-shadow);
    overflow: hidden;
  }

  /* Shared brand lockup */
  .brand-mark {
    position: absolute;
    display: flex; align-items: center; gap: 10px;
    color: var(--brand-orange);
    font-weight: 700;
    font-size: 20px;
    white-space: nowrap;
  }
  .brand-mark__dot {
    width: 24px; height: 24px;
    background: var(--brand-brown);
    border-radius: 4px;
    flex: none;
  }

  /* Front */
  .card--front { left: 70px; top: 110px; }
  .card--front .brand-mark { left: 30px; top: 110px; }
  .divider { position: absolute; left: 0; top: 0; }
  .contact {
    position: absolute; left: 300px; top: 98px;
  }
  .contact__name {
    color: var(--brand-orange);
    font-size: 18px; font-weight: 600;
    margin-bottom: 16px;
    white-space: nowrap;
  }
  .contact__list { list-style: none; }
  .contact__item {
    display: flex; align-items: center; gap: 9px;
    color: var(--ink);
    font-size: 11px;
    line-height: 1;
    margin-bottom: 11px;
    white-space: nowrap;
  }
  .contact__icon { width: 12px; height: 12px; flex: none; }

  /* Back */
  .card--back { left: 590px; top: 490px; }
  .product-shot {
    position: absolute; left: 40px; top: 40px;
    width: 230px; height: 195px;
  }
  .product-shot__box {
    position: absolute;
    border-radius: 6px;
    background: linear-gradient(135deg, var(--kraft-light), var(--kraft));
    box-shadow: 0 4px 10px rgba(0,0,0,.15);
  }
  .product-shot__box--a { left: 0; top: 0; width: 120px; height: 118px; border-bottom: 16px solid var(--grass); }
  .product-shot__box--b { left: 100px; top: 82px; width: 125px; height: 110px; border-left: 14px solid var(--grass); }
  .card--back .brand-mark { left: 290px; top: 72px; }
  .card--back .web {
    position: absolute; left: 40px; top: 262px;
    color: var(--brand-brown);
    font-size: 14px; font-weight: 600;
  }
</style>
</head>
<body>
<main class="stage">

  <section class="card card--front" aria-label="Business card front">
    <svg class="divider" width="540" height="310" aria-hidden="true">
      <line x1="285" y1="45" x2="235" y2="270" stroke="var(--brand-orange)" stroke-width="1.5" stroke-opacity=".8"/>
    </svg>
    <div class="brand-mark">
      <span class="brand-mark__dot"></span>
      <span>Purrlane Nest Co</span>
    </div>
    <div class="contact">
      <p class="contact__name">Purrlane Nest Co</p>
      <ul class="contact__list">
        <li class="contact__item">
          <svg class="contact__icon" viewBox="0 0 24 24" aria-hidden="true"><path fill="var(--brand-orange)" d="M6.6 10.8a15 15 0 0 0 6.6 6.6l2.2-2.2c.3-.3.7-.4 1-.2 1.1.4 2.3.6 3.6.6.6 0 1 .4 1 1V20c0 .6-.4 1-1 1A17 17 0 0 1 3 4c0-.6.4-1 1-1h3.5c.6 0 1 .4 1 1 0 1.3.2 2.5.6 3.6.1.3 0 .7-.2 1z"/></svg>
          +1 (808) 555 0172
        </li>
        <li class="contact__item">
          <svg class="contact__icon" viewBox="0 0 24 24" aria-hidden="true"><path fill="var(--brand-orange)" d="M2 5h20v14H2z"/><path d="M2 5l10 8 10-8" fill="none" stroke="#fff" stroke-width="2"/></svg>
          support@purrlanenestco.example
        </li>
        <li class="contact__item">
          <svg class="contact__icon" viewBox="0 0 24 24" aria-hidden="true"><circle cx="12" cy="12" r="9" fill="none" stroke="var(--brand-orange)" stroke-width="2"/><path d="M3 12h18M12 3c3 3 3 15 0 18M12 3c-3 3-3 15 0 18" fill="none" stroke="var(--brand-orange)" stroke-width="1.5"/></svg>
          www.purrlanenestco.example
        </li>
      </ul>
    </div>
  </section>

  <section class="card card--back" aria-label="Business card back">
    <div class="product-shot" role="img" aria-label="Photo of two kraft-paper cat grass kit boxes">
      <div class="product-shot__box product-shot__box--a"></div>
      <div class="product-shot__box product-shot__box--b"></div>
    </div>
    <div class="brand-mark">
      <span class="brand-mark__dot"></span>
      <span>Purrlane Nest Co</span>
    </div>
    <p class="web">www.purrlanenestco.example</p>
  </section>

</main>
</body>
</html>
```